Salve Label

2.25 inch round label.

We are looking for a simple label, muted natural colors, sophisticated, elegant, calming.

Name of Product: Herbal Beeswax Salve
This scent is lavender - but there will be others scents
Want this label to be adaptable to other scents with simple color and word changes.

Other things to express on the label - all natural, calming, relaxing

Name of the Company: Copper Hollow Farm
2 oz.

```html
<!DOCTYPE html>
<html lang="en">
<head>
<meta charset="utf-8">
<title>Herbal Beeswax Salve – Lavender Label</title>
<link rel="stylesheet" href="https://fonts.googleapis.com/css2?family=Caveat:wght@700&family=Oleo+Script:wght@700&family=Poppins:wght@400;700&family=Great+Vibes&family=Tinos:ital@1&display=swap">
<style>
  :root {
    --canvas: #ffffff;
    --label-cream: #f3f0c1;
    --ring-white: #ffffff;
    --comb-tone: #f1dc8a;
    --ink: #111111;
    --lavender-deep: #8a6bd0;
    --lavender-light: #c77ef0;
    --leaf-green: #8fae7e;
  }
  html, body {
    margin: 0;
    padding: 0;
    width: 1200px;
    height: 1200px;
    overflow: hidden;
    background: var(--canvas);
  }
  .label-sheet {
    display: block;
    width: 1200px;
    height: 1200px;
  }
  .size-note {
    font-family: "Poppins", sans-serif;
    font-weight: 700;
    font-size: 25px;
    fill: var(--ink);
  }
  .label-disc { fill: var(--label-cream); }
  .label-ring { fill: none; stroke: var(--ring-white); stroke-width: 3; }
  .word-herbal {
    font-family: "Caveat", cursive;
    font-weight: 700;
    font-size: 62px;
    fill: var(--ink);
  }
  .word-beeswax {
    font-family: "Oleo Script", cursive;
    font-weight: 700;
    font-size: 118px;
    fill: var(--ink);
    stroke: var(--ring-white);
    stroke-width: 14px;
    stroke-linejoin: round;
    paint-order: stroke fill;
  }
  .word-salve {
    font-family: "Poppins", sans-serif;
    font-weight: 400;
    font-size: 41px;
    fill: #222222;
  }
  .scent-name {
    font-family: "Great Vibes", cursive;
    font-size: 90px;
    stroke: var(--ring-white);
    stroke-width: 4px;
    paint-order: stroke fill;
  }
  .ingredients {
    font-family: "Tinos", serif;
    font-style: italic;
    font-size: 27.5px;
    fill: var(--ink);
  }
  .arc-text {
    font-family: "Tinos", serif;
    font-style: italic;
    font-size: 27.5px;
    fill: var(--ink);
  }
</style>
</head>
<body>
<svg class="label-sheet" viewBox="0 0 1200 1200" xmlns="http://www.w3.org/2000/svg">
  <defs>
    <linearGradient id="scentGradient" x1="0" y1="0" x2="1" y2="0">
      <stop offset="0" stop-color="var(--lavender-deep)"/>
      <stop offset="1" stop-color="var(--lavender-light)"/>
    </linearGradient>
    <linearGradient id="sprigGradient" x1="0" y1="0" x2="0" y2="1">
      <stop offset="0" stop-color="#a08ae0"/>
      <stop offset="0.6" stop-color="#b9a9e4"/>
      <stop offset="1" stop-color="var(--leaf-green)"/>
    </linearGradient>
    <path id="footerArc" d="M 228 672 A 375 375 0 0 0 978 672"/>
  </defs>

  <text class="size-note" x="637" y="208" text-anchor="middle">2.25”</text>

  <g class="round-label">
    <circle class="label-disc" cx="603" cy="672" r="414"/>
    <circle class="label-ring" cx="603" cy="672" r="390"/>

    <path class="honeycomb-area" role="img" aria-label="Faint honeycomb pattern backdrop"
          d="M 560 345 L 700 360 L 860 400 L 885 470 L 880 560 L 885 640 L 860 690 L 770 700 L 690 670 L 600 620 L 510 600 L 470 540 L 430 450 L 470 420 L 560 400 Z"
          fill="var(--comb-tone)" opacity="0.28"/>

    <ellipse class="bee-illustration" role="img" aria-label="Small honeybee illustration"
             cx="650" cy="462" rx="26" ry="20" fill="#b98a3c" opacity="0.55"/>

    <text class="word-herbal" x="425" y="492">Herbal</text>
    <text class="word-beeswax" x="318" y="572" textLength="526" lengthAdjust="spacingAndGlyphs">Beeswax</text>
    <text class="word-salve" x="666" y="628">Salve</text>

    <text class="scent-name" x="456" y="775" fill="url(#scentGradient)" textLength="262" lengthAdjust="spacingAndGlyphs">Lavender</text>
    <rect class="flower-illustration" role="img" aria-label="Watercolour lavender crocus sprig"
          x="720" y="712" width="98" height="108" rx="40" fill="url(#sprigGradient)" opacity="0.7"/>

    <text class="ingredients" text-anchor="middle">
      <tspan x="606" y="875">Ingredients: Homegrown Lavender Blooms,</tspan>
      <tspan x="606" y="912">Sweet almond oil, Comfrey infused olive oil</tspan>
      <tspan x="606" y="947">Beewax, vitamin E</tspan>
    </text>

    <text class="arc-text" text-anchor="middle">
      <textPath href="#footerArc" startOffset="38.5%">Copper Hollow Farm</textPath>
    </text>
    <text class="arc-text" text-anchor="middle">
      <textPath href="#footerArc" startOffset="60%">Net Wt. 2oz</textPath>
    </text>
  </g>
</svg>
</body>
</html>
```